Quorvel Landing page redesign

We are looking for a landing page redesign before we officially launch. We want to incorporate the information already on the site at www.Quorvel.example landing page but make it more inviting. There needs to be a sign up section along with clearly stating what we do. Having a place for sample profiles and linking to our blog and podcast is option. More information about all we will be doing is at Quorvel is on the landing page and also on the blog.

Target Market(s)

35 years old and up.

Coding

Coded - Design and coding required

Number of Pages Required

1 page

Requirements
Must have
• The top bar and the bottom bar (with the privacy policy, etc)
• Sign in/up section.
• I don't want to give to much here because I want designers to be creative.
Nice to have
• Prefer not to have a landing page that requires a lot of scrolling at all.

```html
<!DOCTYPE html>
<html lang="en">
<head>
<meta charset="utf-8">
<title>Quorvel – Share your story</title>
<link href="https://fonts.googleapis.com/css2?family=Raleway:wght@300;400;600;700&display=swap" rel="stylesheet">
<style>
  :root {
    --white: #ffffff;
    --ink: #111111;
    --nav-ink: #3b2a78;
    --lime: #93c01f;
    --leaf: #3f8a35;
    --forest: #056633;
    --rule: #e2e6c8;
  }
  * { margin: 0; padding: 0; box-sizing: border-box; }
  html, body { width: 1200px; height: 806px; overflow: hidden; background: var(--white); }
  body { font-family: "Raleway", sans-serif; }

  .page { position: relative; width: 1200px; height: 806px; overflow: hidden; border: 1px solid var(--rule); }

  .top-bar {
    position: absolute; top: 0; left: 0; right: 0; height: 48px;
    display: flex; justify-content: space-between; align-items: flex-start;
    padding: 22px 82px 0 52px; font-size: 11px; color: var(--nav-ink);
  }
  .top-bar a { color: inherit; text-decoration: none; }
  .nav-links span { margin: 0 6px; }

  .hero {
    position: absolute; top: 48px; left: 0; width: 1200px; height: 728px;
    background: linear-gradient(90deg, var(--lime) 0%, var(--forest) 100%);
    overflow: hidden;
  }
  .hero-shapes { position: absolute; top: 0; left: 0; }

  .headline { position: absolute; left: 148px; top: 56px; width: 284px; color: var(--white); text-align: right; }
  .headline h1 { font-weight: 600; font-size: 72px; letter-spacing: 8px; margin-right: -8px; line-height: 1; }
  .headline p { font-weight: 700; font-size: 16px; margin-top: 4px; }

  .topic { position: absolute; color: var(--white); font-weight: 300; font-size: 27px; line-height: 32px; }
  .topic-stories { left: 255px; top: 200px; }
  .topic-history { left: 393px; top: 336px; }
  .topic-media { left: 529px; top: 470px; }

  .brand-name {
    position: absolute; left: 1022px; top: 308px;
    color: var(--white); font-weight: 400; font-size: 38px; line-height: 46px;
  }
  .sign-up {
    position: absolute; left: 1035px; top: 354px; width: 165px; height: 40px;
    background: var(--white); color: var(--ink);
    clip-path: polygon(0 0, 100% 0, 100% 100%, 16% 100%);
    display: flex; align-items: center; justify-content: flex-end; padding-right: 26px;
    font-size: 18px; text-decoration: none;
  }

  .bottom-bar {
    position: absolute; left: 0; right: 0; bottom: 0; height: 30px;
    display: flex; justify-content: space-between; align-items: center;
    padding: 0 82px 0 52px; font-size: 11px; color: var(--nav-ink);
  }
  .bottom-bar a { color: inherit; text-decoration: none; }
  .bottom-bar span { margin: 0 6px; }
</style>
</head>
<body>
<div class="page">
  <header class="top-bar">
    <nav class="nav-links"><a href="#">Blog</a><span>|</span><a href="#">Podcast</a></nav>
    <a href="#" class="login">Login</a>
  </header>

  <main class="hero">
    <svg class="hero-shapes" width="1200" height="728" viewBox="0 0 1200 728" aria-hidden="true">
      <defs>
        <linearGradient id="panel-shade" x1="0" y1="0" x2="1" y2="0">
          <stop offset="0" stop-color="#3f8a35"/>
          <stop offset="1" stop-color="#056633"/>
        </linearGradient>
      </defs>
      <path class="side-panel" fill="url(#panel-shade)"
            d="M660 0 L1200 0 L1200 728 L640 728 C720 640 820 480 900 372 C860 300 760 120 660 0 Z"/>
      <path class="sweep" fill="#ffffff"
            d="M610 0 L660 0 C760 120 860 300 900 372 C820 480 720 640 640 728 L515 728 C600 700 650 650 690 600 C760 500 830 420 855 372 C800 280 710 120 610 0 Z"/>
      <line x1="0" y1="17" x2="657" y2="657" stroke="#ffffff" stroke-width="6"/>
      <circle cx="211" cy="225" r="29" fill="#ffffff"/>
      <circle cx="350" cy="361" r="29" fill="#ffffff"/>
      <circle cx="487" cy="496" r="29" fill="#ffffff"/>
    </svg>

    <div class="headline">
      <h1>SHARE</h1>
      <p>YOUR QUORVEL</p>
    </div>

    <span class="topic topic-stories">Stories</span>
    <span class="topic topic-history">History</span>
    <span class="topic topic-media">Media</span>

    <span class="brand-name">Quorvel</span>
    <a href="#" class="sign-up">Sign up</a>
  </main>

  <footer class="bottom-bar">
    <nav><a href="#">Privacy Policy</a><span>|</span><a href="#">Terms of Use</a><span>|</span><a href="#">Contact</a></nav>
    <span>www.Quorvel.example</span>
  </footer>
</div>
</body>
</html>
```